Software Company Business Card Design

We are looking for a business card design for a software, messaging & IT services company based in Australia.

Talvora Group is the holding company for 3 brands all offering technology based business solutions; Talvora, Brindle & Quillpad. Brand Identity = Friendly, Professional, Viable, Vibrant, Creative

We want our business card to reflect that we are an innovative market leader. The design should be clean, professional and original.

This design will be used for all 3 brands.

More information about our company can be found at: www.talvoragroup.example.au
www.brindle.example.au

Details we would like on the card:

Firstname Lastname
Position
Level 17, 482 Ormond Rd
North Sydney
NSW 2060
Phone: +61 2 5550 1738
Fax: +61 2 5550 1794
Mobile:
Email:
www.talvoragroup.example.au

Target Market(s)

Our business cards are given to B2B and industry professionals.

Industry/Entity Type

Business

Requirements
Must have
• The Business Card must include the same colours as the logo.
Nice to have
• We would like it to me double sided.

```html
<!DOCTYPE html>
<html lang="en">
<head>
<meta charset="utf-8">
<title>Talvora Group — Business Card</title>
<link href="https://fonts.googleapis.com/css2?family=Open+Sans:wght@400;600;700&display=swap" rel="stylesheet">
<style>
  :root {
    --brand-crimson: #a91d3a;
    --brand-pink: #cf4a6d;
    --ink: #1f1f1f;
    --paper: #ffffff;
    --canvas: #ffffff;
  }
  * { box-sizing: border-box; margin: 0; padding: 0; }
  html, body {
    width: 938px;
    height: 1200px;
    overflow: hidden;
    background: var(--canvas);
    font-family: "Open Sans", Arial, sans-serif;
  }
  .canvas {
    position: relative;
    width: 938px;
    height: 1200px;
  }
  .card {
    position: absolute;
    left: 59px;
    width: 820px;
    height: 524px;
  }
  .card--front {
    top: 40px;
    background: var(--paper);
    border: 1px solid #e4e4e4;
  }
  .card--back {
    top: 620px;
    background: var(--brand-crimson);
  }
  .brand-name {
    position: absolute;
    font-weight: 600;
    letter-spacing: -0.5px;
    line-height: 1;
    white-space: nowrap;
  }
  .card--front .brand-name {
    top: 70px;
    right: 62px;
    font-size: 52px;
    color: var(--brand-crimson);
  }
  .card--back .brand-name {
    left: 38px;
    top: 372px;
    font-size: 60px;
    color: var(--paper);
  }
  .holder {
    position: absolute;
    left: 56px;
    top: 232px;
  }
  .holder__name {
    font-size: 30px;
    font-weight: 600;
    color: var(--brand-crimson);
    line-height: 1.2;
  }
  .holder__position {
    font-size: 15px;
    font-weight: 700;
    color: var(--ink);
    margin-top: 2px;
  }
  .contact {
    position: absolute;
    right: 59px;
    top: 250px;
    text-align: right;
    font-style: normal;
    font-size: 19px;
    line-height: 28px;
    color: var(--ink);
  }
  .services {
    position: absolute;
    right: 59px;
    top: 468px;
    font-size: 14.5px;
    letter-spacing: 0.2px;
    color: var(--brand-pink);
    text-transform: uppercase;
  }
  .card--back .website {
    position: absolute;
    right: 28px;
    bottom: 76px;
    font-size: 18px;
    color: var(--paper);
  }
</style>
</head>
<body>
  <main class="canvas">
    <section class="card card--front" aria-label="Card front">
      <div class="brand-name">Talvora Group</div>
      <div class="holder">
        <div class="holder__name">First Name</div>
        <div class="holder__position">Position</div>
      </div>
      <address class="contact">
        Level 17, 482 Ormond Rd<br>
        North Sydney<br>
        NSW 2060<br>
        Phone: +61 2 5550 1738<br>
        Fax: +61 2 5550 1794<br>
        Mobile: 0491 570 156<br>
        Email: email@talvoragroup.example.au<br>
        www.talvoragroup.example.au
      </address>
      <div class="services">Financial Service Solutions | IT Services | Messaging Solutions</div>
    </section>

    <section class="card card--back" aria-label="Card back">
      <div class="brand-name">Talvora Group</div>
      <div class="website">www.talvoragroup.example.au</div>
    </section>
  </main>
</body>
</html>
```